Webiste Design KDW

Design the website using uploaded content. Design colors should match that of the company logo with an allowance of one more extra color if it makes the website look much better and colorful. Use Technology related stock images in your design.

Target Market(s)

Potential Clients - Companies

Industry/Entity Type

Information Technology

Coding

Coded - Design and coding required

Number of Pages Required

5+ page

Requirements
Must have
• Company Logo Colors
Nice to have
• Professional Look and Feel with Sliders showing professional information technology images

```html
<!DOCTYPE html>
<html lang="en">
<head>
<meta charset="UTF-8">
<title>KDW Technologies</title>
<link href="https://fonts.googleapis.com/css2?family=Poppins:wght@400;500;600;700&display=swap" rel="stylesheet">
<style>
:root{
  --orange:#ff8a00;
  --dark:#2b2b2b;
  --cream:#fff4ea;
  --white:#ffffff;
  --text:#222222;
}
*{margin:0;padding:0;box-sizing:border-box}
html,body{width:1200px;height:4222px;overflow:hidden}
body{font-family:'Poppins',sans-serif;color:var(--text);background:var(--white);position:relative}
.page{position:relative;width:1200px;height:4222px;overflow:hidden}
.bg-shapes{position:absolute;left:0;top:0;width:1200px;height:4222px}
.abs{position:absolute}
.brand{display:flex;align-items:center;gap:12px;color:var(--orange);font-weight:700}
.brand-dot{width:30px;height:30px;border-radius:50%;background:var(--orange);flex:none}
.site-header .brand{left:111px;top:30px;font-size:34px;letter-spacing:1px}
.contact-bar{right:112px;top:26px;display:flex;gap:16px;font-size:19px;font-weight:500}
.contact-item{display:flex;align-items:center;gap:10px}
.icon-circle{width:30px;height:30px;border-radius:50%;background:var(--orange);display:flex;align-items:center;justify-content:center}
.main-nav{right:112px;top:68px;display:flex;gap:22px;font-size:16px;font-weight:500;text-transform:uppercase}
.hero-brand{left:111px;top:200px;color:var(--orange);font-weight:700;font-size:58px;line-height:1.1;width:420px}
.hero-text{left:111px;top:330px;width:360px;font-size:15px;line-height:26px;font-weight:500}
.statement{top:820px;width:466px;color:var(--white)}
.statement h2{font-size:31px;font-weight:600;margin:30px 0 14px;letter-spacing:.3px}
.statement p{font-size:15px;line-height:26px;text-align:justify}
.mission{left:111px}
.vision{left:623px}
.section-title{font-size:31px;font-weight:600;text-transform:uppercase}
.values{left:111px;top:1188px;width:520px}
.values p,.industries p{font-size:15px;line-height:26px;text-align:justify;margin-top:14px}
.bullets{list-style:none;margin-top:14px}
.bullets li{position:relative;padding-left:22px;font-size:15px;line-height:26px;text-align:justify}
.bullets li::before{content:"";position:absolute;left:0;top:10px;width:9px;height:9px;border-radius:50%;background:var(--orange)}
.photo-blob{background:linear-gradient(135deg,#d9d4cf,#8a7f76 60%,#c4492f);border:8px solid var(--white);box-shadow:0 6px 24px rgba(0,0,0,.18)}
.values-photo{left:680px;top:1222px;width:402px;height:408px;border-radius:48% 52% 44% 56%/40% 46% 54% 60%}
.ring{background:var(--dark);border-radius:32%;display:flex;align-items:center;justify-content:center}
.ring span{display:block;border-radius:50%;background:var(--orange)}
.governance-head{left:0;top:1850px;width:1200px;text-align:center;color:var(--white)}
.governance-head p{font-size:15px;line-height:26px;width:960px;margin:18px auto 0}
.card{top:2077px;width:282px;height:324px;background:var(--white);border-radius:22px;text-align:center;padding:110px 12px 0}
.card h3{font-size:20px;font-weight:600}
.card p{font-size:15px;line-height:26px;margin-top:10px}
.card .btn{display:inline-block;margin-top:22px;background:var(--dark);color:var(--white);font-size:15px;font-weight:500;padding:10px 18px;border-radius:30px}
.card-badge{position:absolute;right:-36px;top:-50px;width:150px;height:150px;border-radius:50%;background:var(--orange);border:7px solid var(--dark);display:flex;align-items:center;justify-content:center}
.industries{left:595px;top:2678px;width:492px}
.industries .bullets{margin-top:18px}
.industries .bullets li{font-size:16px;line-height:39px;font-weight:500;padding-left:22px}
.industries .bullets li::before{top:15px}
.industries-photo{left:107px;top:2696px;width:434px;height:432px;border-radius:52% 48% 58% 42%/46% 52% 48% 54%;background:linear-gradient(135deg,#e8e2dc,#b9a89a 55%,#4a4a4a)}
.partners-title{left:0;top:3243px;width:1200px;text-align:center}
.partner-grid{left:111px;top:3331px;width:974px;display:grid;grid-template-columns:repeat(4,222px);column-gap:29px;row-gap:30px}
.partner-badge{height:106px;border:3px solid var(--dark);border-radius:24px;display:flex;align-items:center;justify-content:center}
.partner-badge span{display:block;width:120px;height:40px;border-radius:8px;background:#d9d9d9}
.footer-brand{left:111px;top:3905px;font-size:48px;color:var(--white)}
.footer-brand .brand-dot{width:44px;height:44px}
.region{top:3820px;width:300px;color:var(--white)}
.region h2{font-size:31px;font-weight:600;margin-bottom:14px}
.addr{display:flex;gap:14px;margin-bottom:18px}
.addr h4{font-size:19px;font-weight:500;line-height:24px}
.addr p{font-size:14px;line-height:21px;margin-top:4px}
.pin{flex:none;width:34px;height:34px;border-radius:50%;background:var(--orange);display:flex;align-items:center;justify-content:center}
.limpopo{left:497px}
.gauteng{left:815px}
.footer-rule{left:111px;top:4135px;width:976px;height:2px;background:#8a8a8a}
.copyright{left:0;top:4166px;width:1200px;text-align:center;color:var(--white);font-size:17px;font-weight:500}
</style>
</head>
<body>
<div class="page">
  <svg class="bg-shapes" viewBox="0 0 1200 4222" xmlns="http://www.w3.org/2000/svg">
    <defs>
      <linearGradient id="heroFade" x1="0" y1="0" x2="0" y2="1">
        <stop offset="0" stop-color="#fffdfb"/>
        <stop offset="1" stop-color="#fff1e4"/>
      </linearGradient>
      <linearGradient id="teamTone" x1="0" y1="0" x2="1" y2="1">
        <stop offset="0" stop-color="#cfc6bc"/>
        <stop offset=".5" stop-color="#8b7a69"/>
        <stop offset="1" stop-color="#3d3a38"/>
      </linearGradient>
    </defs>
    <rect x="0" y="0" width="1200" height="800" fill="url(#heroFade)"/>
    <rect x="520" y="160" width="630" height="640" rx="40" fill="url(#teamTone)" role="img" aria-label="Photograph of a business team gathered around a tablet"/>
    <polygon points="0,587 600,728 600,1128 0,1128" fill="var(--dark)"/>
    <polygon points="600,728 893,795 1200,587 1200,1128 600,1128" fill="var(--orange)"/>
    <polygon points="600,728 893,795 893,808 600,741" fill="#1f1f1f"/>
    <polygon points="0,1843 902,1705 1200,1832 1200,1852 902,1722 0,1856" fill="var(--orange)"/>
    <polygon points="0,1856 902,1722 1200,1852 1200,2424 287,2595 0,2474" fill="var(--dark)"/>
    <polygon points="0,2474 287,2595 1200,2424 1200,2440 287,2612 0,2490" fill="var(--orange)"/>
    <polygon points="0,3788 902,3650 1200,3772 1200,3792 902,3666 0,3800" fill="var(--orange)"/>
    <polygon points="0,3800 902,3666 1200,3792 1200,4222 0,4222" fill="var(--dark)"/>
  </svg>

  <header class="site-header">
    <div class="brand abs"><span class="brand-dot"></span>KDW TECHNOLOGIES</div>
    <div class="contact-bar abs">
      <div class="contact-item"><span class="icon-circle"><svg width="16" height="16" viewBox="0 0 24 24"><path d="M6.6 10.8a15 15 0 0 0 6.6 6.6l2.2-2.2a1 1 0 0 1 1-.25 11.4 11.4 0 0 0 3.6.57 1 1 0 0 1 1 1V20a1 1 0 0 1-1 1A17 17 0 0 1 3 4a1 1 0 0 1 1-1h3.5a1 1 0 0 1 1 1c0 1.25.2 2.45.57 3.6a1 1 0 0 1-.25 1z" fill="#fff"/></svg></span>012 555 0147</div>
      <div class="contact-item"><span class="icon-circle"><svg width="16" height="16" viewBox="0 0 24 24"><path d="M6.6 10.8a15 15 0 0 0 6.6 6.6l2.2-2.2a1 1 0 0 1 1-.25 11.4 11.4 0 0 0 3.6.57 1 1 0 0 1 1 1V20a1 1 0 0 1-1 1A17 17 0 0 1 3 4a1 1 0 0 1 1-1h3.5a1 1 0 0 1 1 1c0 1.25.2 2.45.57 3.6a1 1 0 0 1-.25 1z" fill="#fff"/></svg></span>hello@kdwtech.co.za</div>
    </div>
    <nav class="main-nav abs"><span>Home</span><span>Our Values</span><span>Services</span><span>Industries</span><span>Contact Us</span></nav>
  </header>

  <div class="hero-brand abs">KDW Technologies</div>
  <p class="hero-text abs">Our Company is built on the assumption that the management of information technology for business is like legal advice or accounting</p>

  <section class="statement mission abs">
    <svg width="76" height="76" viewBox="0 0 76 76"><circle cx="36" cy="40" r="32" fill="none" stroke="#fff" stroke-width="5"/><circle cx="36" cy="40" r="18" fill="none" stroke="#fff" stroke-width="5"/><circle cx="36" cy="40" r="5" fill="#fff"/><path d="M36 40 L66 10 M58 6 L66 10 L70 18" fill="none" stroke="#fff" stroke-width="5" stroke-linecap="round"/></svg>
    <h2>MISSION STATEMENT</h2>
    <p>To provide and run ICT as well as Engineering solutions and services that allows our customers to focus on achieving their business objectives.</p>
  </section>
  <section class="statement vision abs">
    <svg width="92" height="76" viewBox="0 0 92 76"><path d="M4 38 Q46 -6 88 38 Q46 82 4 38Z" fill="none" stroke="#fff" stroke-width="5"/><circle cx="46" cy="38" r="15" fill="none" stroke="#fff" stroke-width="5"/><circle cx="46" cy="38" r="6" fill="#fff"/></svg>
    <h2>VISION STATEMENT</h2>
    <p>Our vision is to be the most innovative and preferred ICT and Engineering Company. We therefore intend to grow the business locally and internationally.</p>
  </section>

  <section class="values abs">
    <h2 class="section-title">Our Values</h2>
    <p>KDW Technologies is committed to the fair and ethical treatment of employees and stakeholders. This is undertaken through implementation of the following company values:</p>
    <ul class="bullets">
      <li>We intend to be a responsible corporate citizen, fulfilling our obligations as anintegral member of society. Our business decisions give appropriate weight andconsideration to social and environmental impacts.</li>
      <li>We intend to provide products, services and solutions of uncompromising quality.</li>
      <li>We intend to seek mutually beneficial and enduring relationships in all thecommitments that we make, ensuring that they are straightforward and honest. Ourcommunication is open and accurate, both internally and externally.</li>
      <li>We intend to uphold all the above company values, promoting our employees to do likewise.</li>
    </ul>
  </section>
  <div class="photo-blob values-photo abs" role="img" aria-label="Photograph of a smiling man in a checked shirt talking on a phone"></div>
  <div class="ring abs" style="left:959px;top:1205px;width:124px;height:124px"><span style="width:100px;height:100px"></span></div>
  <div class="ring abs" style="left:680px;top:1467px;width:86px;height:84px"><span style="width:62px;height:62px"></span></div>
  <div class="ring abs" style="left:948px;top:1525px;width:62px;height:62px"><span style="width:44px;height:44px"></span></div>

  <section class="governance-head abs">
    <h2 class="section-title">Governance, Risk and Ethics</h2>
    <p>KDW Technologies understands investor concerns and issues of governance; ethics and sustainabilitywhich are also high on our agenda.</p>
  </section>

  <article class="card abs" style="left:111px">
    <div class="card-badge"><svg width="80" height="80" viewBox="0 0 80 80" fill="none" stroke="#fff" stroke-width="3"><circle cx="40" cy="40" r="26"/><circle cx="40" cy="16" r="7"/><circle cx="16" cy="50" r="7"/><circle cx="64" cy="50" r="7"/><path d="M28 66 Q40 50 52 66"/><circle cx="40" cy="46" r="7"/></svg></div>
    <h3>Integrity</h3>
    <p>We believe that all decisions are made with integrity, being honest with self and with others.</p>
    <span class="btn">READ MORE</span>
  </article>
  <article class="card abs" style="left:442px">
    <div class="card-badge"><svg width="80" height="80" viewBox="0 0 80 80" fill="none" stroke="#fff" stroke-width="3"><circle cx="40" cy="38" r="24"/><circle cx="40" cy="38" r="16"/><path d="M14 38 Q14 10 40 10 Q66 10 66 38"/><rect x="10" y="34" width="8" height="14" rx="3"/><rect x="62" y="34" width="8" height="14" rx="3"/><path d="M66 48 Q62 66 44 66"/></svg></div>
    <h3>Customer Service</h3>
    <p>We believe that customers can and will take notice of and appre ciate great, caring service.</p>
    <span class="btn">READ MORE</span>
  </article>
  <article class="card abs" style="left:772px">
    <div class="card-badge"><svg width="80" height="80" viewBox="0 0 80 80" fill="none" stroke="#fff" stroke-width="3"><circle cx="40" cy="48" r="20"/><circle cx="40" cy="48" r="9"/><path d="M40 8 L40 36 M30 18 L40 8 L50 18"/><path d="M18 36 L12 32 M62 36 L68 32 M18 60 L12 64 M62 60 L68 64"/></svg></div>
    <h3>Continuous Improvement</h3>
    <p>We believe in not accepting the status quo; we believe in the value of ongoing training in any form.</p>
    <span class="btn">READ MORE</span>
  </article>

  <div class="photo-blob industries-photo abs" role="img" aria-label="Photograph of a smiling businesswoman in a grey blazer"></div>
  <div class="ring abs" style="left:369px;top:2696px;width:142px;height:142px"><span style="width:108px;height:108px"></span></div>
  <div class="ring abs" style="left:66px;top:2926px;width:90px;height:90px"><span style="width:64px;height:64px"></span></div>
  <div class="ring abs" style="left:374px;top:3065px;width:62px;height:62px"><span style="width:44px;height:44px"></span></div>

  <section class="industries abs">
    <h2 class="section-title">Industries</h2>
    <p>Our "Adaptive Urban Traffic Control System (UTC)" is a leading UTC system in the world. It can control urban traffic signal intelligently by traffic data collection.</p>
    <ul class="bullets">
      <li>Central Control Server Software</li>
      <li>Area Control Server Software</li>
      <li>Communication Server Software</li>
      <li>External Service Server Software</li>
      <li>Simulative Controller Software</li>
      <li>Client Software</li>
      <li>CMT Software</li>
    </ul>
  </section>

  <h2 class="section-title partners-title abs">Partnership</h2>
  <div class="partner-grid abs">
    <div class="partner-badge"><span></span></div>
    <div class="partner-badge"><span></span></div>
    <div class="partner-badge"><span></span></div>
    <div class="partner-badge"><span></span></div>
    <div class="partner-badge"><span></span></div>
    <div class="partner-badge"><span></span></div>
    <div class="partner-badge"><span></span></div>
    <div class="partner-badge"><span></span></div>
  </div>

  <footer>
    <div class="brand footer-brand abs"><span class="brand-dot"></span>KDW</div>
    <section class="region limpopo abs">
      <h2>LIMPOPO</h2>
      <div class="addr"><span class="pin"><svg width="16" height="18" viewBox="0 0 16 20"><path d="M8 0a8 8 0 0 0-8 8c0 6 8 12 8 12s8-6 8-12a8 8 0 0 0-8-8z" fill="#fff"/><circle cx="8" cy="8" r="3" fill="#ff8a00"/></svg></span><div><h4>Physical Address</h4><p>14 Baobab Lane<br>Marula Heights<br>0712</p></div></div>
      <div class="addr"><span class="pin"><svg width="16" height="18" viewBox="0 0 16 20"><path d="M8 0a8 8 0 0 0-8 8c0 6 8 12 8 12s8-6 8-12a8 8 0 0 0-8-8z" fill="#fff"/><circle cx="8" cy="8" r="3" fill="#ff8a00"/></svg></span><div><h4>Postal Address</h4><p>P. O. Box 40281<br>Thorn Valley<br>0715</p></div></div>
    </section>
    <section class="region gauteng abs">
      <h2>GAUTENG</h2>
      <div class="addr"><span class="pin"><svg width="16" height="18" viewBox="0 0 16 20"><path d="M8 0a8 8 0 0 0-8 8c0 6 8 12 8 12s8-6 8-12a8 8 0 0 0-8-8z" fill="#fff"/><circle cx="8" cy="8" r="3" fill="#ff8a00"/></svg></span><div><h4>Physical Address</h4><p>Block 9 Acacia Office Park<br>Riverlea North<br>2061</p></div></div>
      <div class="addr"><span class="pin"><svg width="16" height="18" viewBox="0 0 16 20"><path d="M8 0a8 8 0 0 0-8 8c0 6 8 12 8 12s8-6 8-12a8 8 0 0 0-8-8z" fill="#fff"/><circle cx="8" cy="8" r="3" fill="#ff8a00"/></svg></span><div><h4>Postal Address</h4><p>Po Box 3390<br>Hillcrest Ridge<br>2068</p></div></div>
    </section>
    <div class="footer-rule abs"></div>
    <p class="copyright abs">Copyrights @ 2023 KDW Technologies.</p>
  </footer>
</div>
</body>
</html>
```